FRESH WEB DESIGN FOR A HEALTH - SOCIAL NETWORK

We are currently looking for a creative, fresh, vibrant, inspiring design for a new social network focused on health and nutrition for health professionals (namely nutritionists) and end-users.

Design requirements - IMPORTANT: please see attached file 'LumaCrest web site design scope' for the detailed brief.

The web site requires new design templates with inter-changeable banners and in some cases profile images. It's important for the website to communicate LumaCrest's core values and image which includes fun, vitality, freshness, life fulfillment, trust, integrity and loyalty to the two target groups. Imagery must have a consistent/inter-related theme across all communities, topics and resources, which need to be easily applied to the web site.To help engage our audience we are looking for something fresh and unique in the selected imagery/ theme/ design templates.

The chosen design will need to be applied to create a PDF, PowerPoint and business card template.

Please see attached file 'LumaCrest web site design scope' to view the LumaCrest web site, which is currently under development.

Nutrition

```html
<!DOCTYPE html>
<html lang="en">
<head>
<meta charset="utf-8">
<title>LumaCrest</title>
<link href="https://fonts.googleapis.com/css2?family=Roboto:wght@300;400;500;700&display=swap" rel="stylesheet">
<style>
:root{
  --blue:#0996d5;
  --blue-dark:#0784bd;
  --green:#8cc63e;
  --green-text:#6aa518;
  --ink:#333333;
  --body:#555555;
  --rule:#e2e2e2;
  --page:#ffffff;
  --foot-text:#e8f5fc;
}
*{margin:0;padding:0;box-sizing:border-box}
html,body{width:817px;height:1200px;overflow:hidden}
body{
  font-family:"Roboto",Arial,sans-serif;
  background:
    radial-gradient(ellipse 260px 420px at 40px 150px,#cfe9dc 0%,rgba(207,233,220,0) 70%),
    radial-gradient(ellipse 220px 420px at 790px 180px,#7cc94a 0%,rgba(124,201,74,0) 75%),
    linear-gradient(180deg,#b9dfd2 0%,#d8eee3 25%,#f4f9f3 45%,#ffffff 60%,#eef7e8 82%,#b7df92 100%);
  position:relative;
}
.page{position:absolute;left:128px;top:0;width:560px;height:1200px;background:var(--page);box-shadow:0 0 8px rgba(0,0,0,.12)}
.abs{position:absolute}

/* header */
.hero{left:0;top:0;width:560px;height:310px;background:linear-gradient(100deg,#ffffff 0%,#f7f4f1 30%,#d9b8a2 45%,#9ad9b8 60%,#f4efe9 78%,#ffffff 100%)}
.brand{left:20px;top:25px;display:flex;align-items:center;gap:6px}
.brand-dot{width:26px;height:26px;border-radius:50%;background:var(--blue)}
.brand-name{font-size:30px;font-weight:500;color:var(--green);letter-spacing:-.5px}
.promo{left:344px;top:42px;width:174px;height:104px;background:#f4f6f7;box-shadow:0 1px 4px rgba(0,0,0,.12);padding:6px 12px}
.promo-big{font-size:26px;font-weight:300;line-height:25px;color:var(--blue);letter-spacing:1px}
.promo-small{font-size:11px;font-weight:300;color:#6a6a6a;letter-spacing:1.1px;margin-top:3px;white-space:nowrap}
.dots{left:25px;top:254px;display:flex;gap:6px}
.dots span{width:8px;height:8px;border-radius:50%;background:#b5b5b5}
.dots span.on{width:9px;height:9px;background:#444}

/* nav */
.nav{left:0;top:310px;width:560px;height:29px;background:var(--blue)}
.nav a{position:absolute;top:9px;font-size:10px;color:#fff;text-decoration:none}
.search{left:422px;top:6px;width:82px;height:18px;background:#fff}
.search-btn{left:504px;top:6px;width:36px;height:18px;background:var(--green);color:#fff;font-size:8px;font-weight:500;text-align:center;line-height:18px}

/* features */
.feature{top:372px;width:165px}
.feature-head{display:flex;align-items:center;gap:7px;font-size:12px;color:var(--ink);white-space:nowrap}
.feature p{font-size:8px;line-height:11.5px;color:var(--body);margin-top:13px}
.rule{height:1px;background:var(--rule)}

/* support */
.photo{border:3px solid #fff;box-shadow:0 0 3px rgba(0,0,0,.3)}
.support-img{left:14px;top:487px;width:146px;height:98px;background:linear-gradient(120deg,#fbfbfb,#f0d9c6 40%,#f3dc5a 55%,#fafafa)}
.support-title{left:177px;top:489px;font-size:12px;color:var(--blue)}
.support-text{left:177px;top:513px;width:172px;font-size:8px;line-height:11.5px;color:var(--body)}
.more{font-size:8px;font-weight:700;color:var(--green-text)}
.support-list{left:367px;top:480px;width:180px;height:128px;border-left:1px solid #ececec;box-shadow:-4px 0 6px -4px rgba(0,0,0,.12);padding-left:13px}
.support-list .title{font-size:8px;color:var(--green-text);margin-top:13px}
.support-list li{list-style:none;font-size:8px;color:#555;margin-top:17px;display:flex;align-items:center;gap:5px}

/* cards */
.section-title{font-size:12px;color:var(--ink)}
.card{width:100px}
.card .thumb{width:100px;height:52px}
.card h4{font-size:8px;font-weight:500;color:#333;margin-top:12px;white-space:nowrap}
.card p{font-size:8px;line-height:10.5px;color:#666;margin-top:4px}

/* resources */
.res-head{left:384px;top:648px;display:flex;align-items:center;gap:6px;font-size:12px;color:var(--ink)}
.res{left:383px;width:165px;display:flex;gap:5px}
.res .thumb{width:36px;height:31px;flex:none;border:2px solid #fff;box-shadow:0 0 2px rgba(0,0,0,.35)}
.res h5{font-size:7.5px;font-weight:700;color:#333}
.res p{font-size:7.5px;line-height:10px;color:#555;margin-top:1px}

/* footer */
.footer{left:0;top:1007px;width:560px;height:171px;background:var(--blue);color:var(--foot-text)}
.foot-sep{top:20px;width:1px;height:140px;background:var(--blue-dark);box-shadow:1px 0 0 rgba(255,255,255,.12)}
.foot-title{font-size:12px;font-weight:500;color:#fff}
.post{left:14px;display:flex;align-items:center;gap:9px;font-size:8px;color:#e4f3fb;width:160px}
.post .thumb{width:22px;height:18px;border:1px solid #fff;flex:none;background:linear-gradient(135deg,#f0d2b8,#a06a4c)}
.contact{left:203px;display:flex;gap:7px;font-size:8px;line-height:10px;color:#fff;width:150px}
.social{left:203px;top:1139px;display:flex;gap:12px}
.social span{width:10px;height:10px;border-radius:50%;background:#d7eefa}
.email-field{left:386px;top:1089px;width:160px;height:20px;background:#fff;font-size:7.5px;color:#aaa;padding:6px 10px}
.foot-brand{left:392px;top:1120px;font-size:16px;font-weight:500;color:#5fb7e3}
.submit{left:500px;top:1121px;width:48px;height:18px;border:1px solid #fff;border-radius:3px;font-size:8px;color:#fff;text-align:center;line-height:16px}
.copy{left:0;top:1178px;width:560px;height:22px;background:var(--green);color:#fff;font-size:8px;text-align:center;line-height:22px}
</style>
</head>
<body>
<div class="page">

  <header>
    <div class="abs hero" role="img" aria-label="Banner photo of a smiling young woman giving a thumbs up while holding a card"></div>
    <div class="abs brand"><span class="brand-dot"></span><span class="brand-name">LumaCrest</span></div>
    <div class="abs promo">
      <div class="promo-big">SHARE<br>YOUR<br>STORY</div>
      <div class="promo-small">AND SUPPORT OTHERS</div>
    </div>
    <div class="abs dots"><span></span><span></span><span></span><span></span><span class="on"></span></div>
  </header>

  <nav class="abs nav">
    <a style="left:20px">Home</a><a style="left:68px">Pages</a><a style="left:117px">Features</a>
    <a style="left:177px">Blog</a><a style="left:219px">Portfolio</a><a style="left:278px">Community</a>
    <div class="abs search"></div><div class="abs search-btn">Search</div>
  </nav>

  <section>
    <div class="abs feature" style="left:14px">
      <div class="feature-head"><svg width="19" height="19" viewBox="0 0 20 20"><circle cx="10" cy="10" r="9.5" fill="#555"/><path d="M5 7c3-2 5 1 4 3s2 3 1 6M11 3c2 2 5 3 6 6" stroke="#fff" stroke-width="1.4" fill="none"/></svg>Live-in Care</div>
      <p>Mauris tristique ex at nisi tincidunt, sed accumsan sapien suscipit. Nulla rhoncus, nulla sit amet consequat tempor</p>
    </div>
    <div class="abs feature" style="left:200px">
      <div class="feature-head"><svg width="22" height="20" viewBox="0 0 22 20"><path d="M11 2a8 8 0 1 1-7.5 5.2" stroke="#555" stroke-width="1.6" fill="none"/><text x="11" y="13" font-size="7" font-family="Roboto,Arial,sans-serif" font-weight="700" fill="#555" text-anchor="middle">24</text></svg>Daily Support</div>
      <p>Mauris tristique ex at nisi tincidunt, sed accumsan sapien suscipit. Nulla rhoncus, nulla sit amet consequat tempor</p>
    </div>
    <div class="abs feature" style="left:386px">
      <div class="feature-head"><svg width="20" height="16" viewBox="0 0 20 16"><circle cx="10" cy="4" r="3" fill="#555"/><circle cx="4" cy="6" r="2.3" fill="#555"/><circle cx="16" cy="6" r="2.3" fill="#555"/><path d="M5 16c0-5 10-5 10 0zM0 15c0-4 6-4 6-1v1zM20 15c0-4-6-4-6-1v1z" fill="#555"/></svg>Professional Assistance</div>
      <p>Mauris tristique ex at nisi tincidunt, sed accumsan sapien suscipit. Nulla rhoncus, nulla sit amet consequat tempor</p>
    </div>
    <div class="abs rule" style="left:14px;top:459px;width:532px"></div>
  </section>

  <section>
    <div class="abs photo support-img" role="img" aria-label="Photo of a woman relaxing on the floor with fresh fruit"></div>
    <h3 class="abs support-title" style="font-weight:400">Support And Educate</h3>
    <p class="abs support-text">Mauris tristique ex at nisi tincidunt, sed accumsan sapien suscipit. Nulla rhoncus, nulla sit amet consequat tempor, odio mi iaculis ipsum, eget porta risus enim sed ante. Aenean laoreet, neque id interdum<br><span class="more" style="display:inline-block;margin-top:6px">read more »</span></p>
    <ul class="abs support-list">
      <div class="title">Support And Educate</div>
      <li><span style="color:var(--green)">»</span>Health Problems Question Answer</li>
      <li><span style="color:var(--green)">»</span>Appropriate Health Care For Adults</li>
      <li><span style="color:var(--green)">»</span>Nursing Services</li>
    </ul>
    <div class="abs rule" style="left:14px;top:617px;width:532px"></div>
  </section>

  <section>
    <h3 class="abs section-title" style="left:16px;top:648px;font-weight:400">Nutritional Therapists</h3>
    <div class="abs card" style="left:14px;top:673px"><div class="thumb photo" role="img" aria-label="Photo of a nutritionist holding an apple" style="background:linear-gradient(90deg,#fff,#e9c3a6 50%,#d44)"></div><h4>Nam Dapibus Rhons Risus</h4><p>Aenean vel mollis lectus. Fus ce scelerisque ipsum ut nisi blandit volutpat...</p></div>
    <div class="abs card" style="left:132px;top:673px"><div class="thumb photo" role="img" aria-label="Photo of a therapist with a bowl of vegetables" style="background:linear-gradient(90deg,#f4f4f4,#e8cbb4 50%,#f4f4f4)"></div><h4>Nam Dapibus Rhons Risus</h4><p>Aenean vel mollis lectus. Fus ce scelerisque ipsum ut nisi blandit volutpat...</p></div>
    <div class="abs card" style="left:251px;top:673px"><div class="thumb photo" role="img" aria-label="Photo of a smiling woman with citrus fruit" style="background:linear-gradient(90deg,#fbfbfb,#f2d6a0 45%,#b4d65a)"></div><h4>Nam Dapibus Rhons Risus</h4><p>Aenean vel mollis lectus. Fus ce scelerisque ipsum ut nisi blandit volutpat...</p></div>
    <div class="abs more" style="left:14px;top:789px">View all »</div>
    <div class="abs rule" style="left:14px;top:820px;width:338px"></div>

    <h3 class="abs section-title" style="left:16px;top:835px;font-weight:400">Success Stories</h3>
    <div class="abs card" style="left:14px;top:861px"><div class="thumb photo" role="img" aria-label="Photo of a woman talking with a doctor" style="background:linear-gradient(90deg,#e7d8cf,#8a5e4c 40%,#8aa2be)"></div><h4>Nam Dapibus Rhons Risus</h4><p>Aenean vel mollis lectus. Fus ce scelerisque ipsum ut nisi blandit volutpat...</p></div>
    <div class="abs card" style="left:132px;top:861px"><div class="thumb photo" role="img" aria-label="Photo of a senior woman outdoors in a garden" style="background:linear-gradient(90deg,#5c8a36,#d9c6b8 50%,#4f7b2c)"></div><h4>Nam Dapibus Rhons Risus</h4><p>Aenean vel mollis lectus. Fus ce scelerisque ipsum ut nisi blandit volutpat...</p></div>
    <div class="abs card" style="left:251px;top:861px"><div class="thumb photo" role="img" aria-label="Portrait photo of a woman" style="background:linear-gradient(90deg,#3a2d1e,#b08468 50%,#2f2a22)"></div><h4>Nam Dapibus Rhons Risus</h4><p>Aenean vel mollis lectus. Fus ce scelerisque ipsum ut nisi blandit volutpat...</p></div>
    <div class="abs more" style="left:14px;top:976px">View all »</div>
  </section>

  <aside>
    <h3 class="abs res-head" style="font-weight:400"><svg width="14" height="14" viewBox="0 0 14 14"><circle cx="7" cy="7" r="7" fill="var(--blue)"/><path d="M7 3.5v7M3.5 7h7" stroke="#fff" stroke-width="1.8"/></svg>Available Resources</h3>
    <div class="abs res" style="top:683px"><div class="thumb" role="img" aria-label="Photo of a family meal" style="background:linear-gradient(135deg,#f6e0c8,#c9855a)"></div><div><h5>Aliquam lacinia nunc eget cons</h5><p>Curabitur malesuada tempor mi ut finibus. Aliquam porttitor est erat, nec sagittis tellus dignissim ut.</p></div></div>
    <div class="abs res" style="top:740px"><div class="thumb" role="img" aria-label="Photo of hands holding a small house" style="background:linear-gradient(135deg,#e9d3c2,#9a6e52)"></div><div><h5>Aliquam lacinia nunc eget cons</h5><p>Curabitur malesuada tempor mi ut finibus. Aliquam porttitor est erat, nec sagittis tellus dignissim ut.</p></div></div>
    <div class="abs res" style="top:796px"><div class="thumb" role="img" aria-label="Photo of a woman resting on a sofa" style="background:linear-gradient(135deg,#6b5a4c,#d2b7a2)"></div><div><h5>Aliquam lacinia nunc eget cons</h5><p>Curabitur malesuada tempor mi ut finibus. Aliquam porttitor est erat, nec sagittis tellus dignissim ut.</p></div></div>
    <div class="abs res" style="top:852px"><div class="thumb" role="img" aria-label="Photo of fresh fruit and vegetables" style="background:linear-gradient(135deg,#7fbf3a,#f2b33a 50%,#e0412f)"></div><div><h5>Aliquam lacinia nunc eget cons</h5><p>Curabitur malesuada tempor mi ut finibus. Aliquam porttitor est erat, nec sagittis tellus dignissim ut.</p></div></div>
    <div class="abs res" style="top:912px"><div class="thumb" role="img" aria-label="Photo of a woman holding a green apple" style="background:linear-gradient(135deg,#f7f7f7,#e6b9c4 50%,#9ccb4a)"></div><div><h5>Aliquam lacinia nunc eget cons</h5><p>Curabitur malesuada tempor mi ut finibus. Aliquam porttitor est erat, nec sagittis tellus dignissim ut.</p></div></div>
    <div class="abs more" style="left:383px;top:976px">View all »</div>
  </aside>

  <footer>
    <div class="abs footer"></div>
    <div class="abs foot-sep" style="left:189px;top:1027px"></div>
    <div class="abs foot-sep" style="left:371px;top:1027px"></div>

    <h3 class="abs foot-title" style="left:14px;top:1031px">Latest Post</h3>
    <div class="abs post" style="top:1057px"><span class="thumb" role="img" aria-label="Post thumbnail"></span>Curabitur ac neque at arcu vesti</div>
    <div class="abs post" style="top:1079px"><span class="thumb" role="img" aria-label="Post thumbnail"></span>Proin vel mauris diam&nbsp; habitasse</div>
    <div class="abs post" style="top:1102px"><span class="thumb" role="img" aria-label="Post thumbnail"></span>Proin urna enim semper posuere</div>
    <div class="abs post" style="top:1125px"><span class="thumb" role="img" aria-label="Post thumbnail"></span>Nunc adipiscing semper nisl</div>
    <div class="abs" style="left:147px;top:1153px;font-size:8px;color:#fff"><u>View all</u> »</div>

    <h3 class="abs foot-title" style="left:205px;top:1031px">Contact Us</h3>
    <div class="abs contact" style="top:1062px"><svg width="10" height="10" viewBox="0 0 10 10"><path d="M5 1 0 5h1.5v4h2.5V6.5h2V9h2.5V5H10z" fill="#fff"/></svg><span>345- Cras mattis facilisis lectus, ultricies ultrices velit pulvinar at</span></div>
    <div class="abs contact" style="top:1091px"><svg width="10" height="10" viewBox="0 0 10 10"><path d="M2 0.5 3.8 2.6 2.8 4a6 6 0 0 0 3.2 3.2l1.4-1 2.1 1.8-1.2 1.6C4.5 9.5.5 5.5.4 1.7z" fill="#fff"/></svg>(800)555-0142</div>
    <div class="abs contact" style="top:1112px"><svg width="10" height="8" viewBox="0 0 10 8"><rect width="10" height="8" fill="#fff"/><path d="M0 0 5 4.5 10 0" stroke="#0996d5" fill="none"/></svg>info@lumacrest.com</div>
    <div class="abs social"><span></span><span></span><span></span><span></span></div>

    <h3 class="abs foot-title" style="left:384px;top:1031px">Subscribe Newsletter</h3>
    <p class="abs" style="left:383px;top:1059px;width:170px;font-size:8px;line-height:10px;color:#fff">Enter your email address to receive all news from our awesome website</p>
    <div class="abs email-field">enter email address</div>
    <div class="abs foot-brand">LumaCrest</div>
    <div class="abs submit">Submit</div>

    <div class="abs copy">Copyright © 2014, All rights reserved.</div>
  </footer>
</div>
</body>
</html>
```